data and media shredding company needs a flyer design

We need a flyer design for a startup company based on Long Island, NY. We shred all types of storage devices at the customers location. We want to emphasize on the dangers of identity theft and confidential information. With some focus on e-waste recycling. We want to coordinate the flyer with our website design.
www.corvellshredworks.example

Target Market(s)

business owners that have personal information that needs to be destroyed

Font styles to use
Sans Serif

Colors

Designer to choose colors to be used in the design.

Requirements
Must have
• must have company name and logo, must have web address, must have phone number 855-301-9648, must have briefing of what we do, must be set for a trifold flyer

```html
<!DOCTYPE html>
<html lang="en">
<head>
<meta charset="utf-8">
<title>Corvell Shredworks – Trifold Flyer</title>
<link href="https://fonts.googleapis.com/css2?family=Lato:ital,wght@0,400;0,700;0,900;1,700&display=swap" rel="stylesheet">
<style>
  :root {
    --stage: #dcdcdc;
    --lime: #7dfb7e;
    --purple: #4b1a5e;
    --yellow: #f4e23c;
    --navy: #2d3966;
    --navy-dark: #1c2447;
    --paper: #eceeee;
    --icon-green: #8cc63f;
    --tag-green: #3b9a2c;
    --white: #ffffff;
  }
  * { box-sizing: border-box; margin: 0; padding: 0; }
  html, body { width: 993px; height: 1200px; overflow: hidden; }
  body {
    background: var(--stage);
    font-family: "Lato", Arial, sans-serif;
    position: relative;
  }
  .sheet {
    position: absolute;
    left: 271px;
    width: 450px;
    height: 582px;
    overflow: hidden;
    box-shadow: 0 6px 18px rgba(0,0,0,.15);
  }
  .sheet--outside { top: 12px; background: var(--lime); }
  .sheet--inside { top: 606px; background: var(--paper); }
  .fold {
    position: absolute; left: 0; width: 100%; height: 1px;
    background: rgba(0,0,0,.07);
  }
  .fold--one { top: 194px; }
  .fold--two { top: 388px; }

  /* Outside */
  .brand {
    position: absolute; top: 10px; right: 14px;
    display: flex; align-items: center; gap: 6px;
    font-size: 12px; font-weight: 700; color: var(--purple);
  }
  .brand__dot { width: 12px; height: 12px; border-radius: 50%; background: var(--purple); }
  .drive-photo {
    position: absolute; top: 66px; left: 190px;
    width: 170px; height: 150px;
    background: radial-gradient(circle at 55% 50%, #d7d3df 0%, #8a8497 55%, #3e3550 100%);
  }
  .particles {
    position: absolute; top: 160px; left: 40px;
    width: 230px; height: 200px;
    background: radial-gradient(ellipse at 70% 30%, rgba(75,26,94,.55) 0%, rgba(75,26,94,.25) 45%, rgba(75,26,94,0) 72%);
  }
  .headline-top {
    position: absolute; top: 36px; right: 16px;
    font-size: 66px; font-weight: 900; color: var(--white);
    letter-spacing: -1px; line-height: 1;
  }
  .headline-band {
    position: absolute; top: 118px; left: 120px;
    background: var(--yellow);
    padding: 4px 16px;
    transform: rotate(4deg);
    font-size: 44px; font-weight: 900; color: var(--purple);
    line-height: 1;
  }
  .headline-safe {
    position: absolute; top: 398px; left: 30px;
    font-size: 88px; font-weight: 900; color: var(--purple); line-height: 1;
  }
  .contact-phone {
    position: absolute; top: 494px; left: 32px;
    font-size: 24px; font-weight: 900; color: var(--purple);
  }
  .contact-web {
    position: absolute; top: 528px; left: 32px;
    font-size: 16px; font-weight: 700; color: var(--purple);
  }

  /* Inside */
  .services {
    position: absolute; top: 0; left: 0; width: 100%; height: 194px;
    display: flex; justify-content: space-around; padding: 20px 10px 0;
  }
  .service { width: 130px; text-align: center; }
  .service__icon { width: 86px; height: 96px; display: block; margin: 0 auto 8px; }
  .service__label { font-size: 13px; font-weight: 900; color: var(--purple); line-height: 1.2; }
  .why {
    position: absolute; top: 194px; left: 0; width: 100%; height: 200px;
    background: linear-gradient(135deg, var(--navy) 0%, var(--navy-dark) 100%);
  }
  .why__title {
    position: absolute; top: 18px; left: 24px;
    font-size: 28px; font-weight: 900; color: var(--white);
  }
  .why__list {
    position: absolute; top: 62px; left: 40px;
    list-style: disc; color: var(--white);
    font-size: 12px; font-weight: 700; font-style: italic; line-height: 1.5;
  }
  .promise {
    position: absolute; top: 380px; left: 0; width: 100%; height: 62px;
    background: var(--yellow);
    display: flex; align-items: center; gap: 12px; padding: 0 24px;
    color: var(--purple);
  }
  .promise__figure { font-size: 46px; font-weight: 900; line-height: 1; }
  .promise__text { font-size: 17px; line-height: 1.15; }
  .badges {
    position: absolute; top: 468px; left: 0; width: 100%;
    display: flex; justify-content: center; align-items: center; gap: 60px;
  }
  .badge--round { width: 34px; height: 34px; border-radius: 50%; background: #6f9aa8; }
  .badge--square { width: 60px; height: 34px; background: #2c4a7a; }
  .tagline {
    position: absolute; top: 526px; left: 0; width: 100%;
    text-align: center; font-size: 22px; font-weight: 700; font-style: italic;
    color: var(--tag-green);
  }
</style>
</head>
<body>

<section class="sheet sheet--outside" aria-label="Flyer outside">
  <div class="fold fold--one"></div>
  <div class="fold fold--two"></div>
  <div class="brand"><span class="brand__dot"></span>Corvell Shredworks</div>
  <div class="drive-photo" role="img" aria-label="Photo of an opened hard drive platter"></div>
  <div class="particles" role="img" aria-label="Hard drive dissolving into scattered particles"></div>
  <h1 class="headline-top">KEEP YOUR</h1>
  <div class="headline-band">INFORMATION</div>
  <div class="headline-safe">SAFE</div>
  <div class="contact-phone">855-301-9648</div>
  <div class="contact-web">www.corvellshredworks.example</div>
</section>

<section class="sheet sheet--inside" aria-label="Flyer inside">
  <div class="fold fold--one"></div>
  <div class="fold fold--two"></div>

  <div class="services">
    <div class="service">
      <svg class="service__icon" viewBox="0 0 86 96" fill="none" stroke="var(--icon-green)" stroke-width="2.5">
        <rect x="18" y="4" width="50" height="52"/>
        <line x1="26" y1="16" x2="40" y2="16"/><line x1="26" y1="26" x2="56" y2="26"/>
        <line x1="26" y1="36" x2="56" y2="36"/><line x1="26" y1="46" x2="48" y2="46"/>
        <rect x="6" y="56" width="74" height="12"/>
        <path d="M14 72v18M22 72v14M30 72v20M38 72v12M46 72v18M54 72v14M62 72v20M70 72v12"/>
      </svg>
      <div class="service__label">Commercial Hard Drive Destruction</div>
    </div>
    <div class="service">
      <svg class="service__icon" viewBox="0 0 86 96" fill="none" stroke="var(--icon-green)" stroke-width="2.5">
        <rect x="33" y="4" width="20" height="14"/>
        <rect x="28" y="18" width="30" height="38"/>
        <rect x="6" y="56" width="74" height="12"/>
        <path d="M14 72v18M22 72v14M30 72v20M38 72v12M46 72v18M54 72v14M62 72v20M70 72v12"/>
      </svg>
      <div class="service__label">Electronic Media Destruction</div>
    </div>
    <div class="service">
      <svg class="service__icon" viewBox="0 0 86 96" fill="none" stroke="var(--icon-green)" stroke-width="2.5">
        <rect x="16" y="4" width="54" height="52" rx="3"/>
        <circle cx="43" cy="30" r="16"/><circle cx="43" cy="30" r="4"/>
        <rect x="6" y="56" width="74" height="12"/>
        <path d="M14 72v18M22 72v14M30 72v20M38 72v12M46 72v18M54 72v14M62 72v20M70 72v12"/>
      </svg>
      <div class="service__label">Paper &amp; Other Confidential Material</div>
    </div>
  </div>

  <div class="why" role="img" aria-label="Close-up photo of a hard drive platter">
    <h2 class="why__title">WHY CHOOSE US?</h2>
    <ul class="why__list">
      <li>Bonded &amp; Insured</li>
      <li>Secure on-site mobile shredding service</li>
      <li>Highest Level Of Security Standards</li>
      <li>State Environmental Registration</li>
      <li>Certified By The National Records Shredding Council (NRSC)</li>
    </ul>
  </div>

  <div class="promise">
    <span class="promise__figure">100%</span>
    <span class="promise__text">Secure Compliant Absolute<br>Data Destruction On-Site</span>
  </div>

  <div class="badges">
    <span class="badge--round"></span>
    <span class="badge--round"></span>
    <span class="badge--square"></span>
  </div>
  <p class="tagline">Any Where, Any Place, Any Time!</p>
</section>

</body>
</html>
```